Business Card Design

An energy company designed around renewable energy and energy storage that focuses on providing its energy at points on the grid that reduce costs and add value to the system.

Industry/Entity Type

Business

Contact Information for Business Card

Martin Dellacroix
Executive Vice President
41 K ST NE
Washington, DC 20017
240-555-0187
mdellacroix@brightvaleenergy.example

```html
<!DOCTYPE html>
<html lang="en">
<head>
<meta charset="utf-8">
<title>Brightvale Energy Company — Business Card</title>
<link href="https://fonts.googleapis.com/css2?family=Open+Sans:wght@400;600;700;800&display=swap" rel="stylesheet">
<style>
  :root {
    --green: #2a7d22;
    --green-dark: #23691c;
    --ink: #1f3d55;
    --ink-soft: #5f7384;
    --grey-band: #e6e6e6;
    --paper: #ffffff;
    --backdrop: #ecebe8;
    --logo-dark: #1c1c1c;
  }
  * { box-sizing: border-box; margin: 0; padding: 0; }
  html, body { width: 1200px; height: 873px; overflow: hidden; }
  body {
    background: var(--backdrop);
    font-family: "Open Sans", Arial, sans-serif;
    position: relative;
  }
  .card {
    position: absolute;
    top: 282px;
    width: 540px;
    height: 309px;
    background: var(--paper);
    box-shadow: 0 6px 18px rgba(0,0,0,0.18);
    overflow: hidden;
  }
  .card--front { left: 40px; }
  .card--back { left: 620px; }
  .card svg.shape { position: absolute; inset: 0; }

  /* Front */
  .front-brand {
    position: absolute;
    left: 0; right: 0; top: 118px;
    display: flex; align-items: center; justify-content: center; gap: 12px;
  }
  .brand-dot {
    width: 34px; height: 34px; border-radius: 50%;
    background: var(--green);
  }
  .brand-text { display: flex; flex-direction: column; line-height: 1; }
  .brand-name {
    font-weight: 800; font-size: 34px; color: var(--logo-dark); letter-spacing: -0.5px;
  }
  .brand-sub {
    font-weight: 800; font-size: 17px; color: var(--logo-dark); margin-top: 4px; letter-spacing: 1px;
  }

  /* Back */
  .holder {
    position: absolute; right: 40px; top: 26px; text-align: right;
  }
  .holder-name {
    font-weight: 800; font-size: 25px; color: var(--ink); letter-spacing: 0.5px;
    text-transform: uppercase;
  }
  .holder-title {
    font-size: 13px; color: var(--ink-soft);
    border-top: 1.5px solid var(--ink); margin-top: 4px; padding-top: 3px;
  }
  .contact-band {
    position: absolute; left: 0; top: 112px; width: 100%; height: 64px;
    background: var(--grey-band);
    border-top: 2px solid var(--green);
    border-bottom: 2px solid var(--green);
    display: flex; align-items: center; gap: 12px; padding-left: 40px;
  }
  .contact-icons { display: flex; flex-direction: column; gap: 4px; }
  .contact-icons svg { display: block; }
  .contact-lines { font-weight: 700; font-size: 12.5px; color: var(--ink); line-height: 1.55; }
  .office {
    position: absolute; left: 40px; top: 196px; font-size: 12px; color: var(--ink-soft); line-height: 1.45;
  }
  .office-name { font-weight: 700; font-size: 13.5px; color: var(--ink); }
  .back-brand {
    position: absolute; right: 36px; bottom: 34px;
    display: flex; align-items: center; gap: 8px; color: var(--paper);
  }
  .back-brand .brand-dot { width: 22px; height: 22px; background: var(--paper); }
  .back-brand .brand-name { color: var(--paper); font-size: 19px; font-weight: 800; }
  .back-brand .brand-sub { color: var(--paper); font-size: 11px; font-weight: 800; }
</style>
</head>
<body>

<section class="card card--front" aria-label="Card front">
  <svg class="shape" width="540" height="309" viewBox="0 0 540 309" aria-hidden="true">
    <path d="M300 0 H540 V175 C500 95 420 25 300 0 Z" fill="var(--green)"/>
  </svg>
  <div class="front-brand">
    <span class="brand-dot"></span>
    <div class="brand-text">
      <span class="brand-name">brightvale energy</span>
      <span class="brand-sub">company</span>
    </div>
  </div>
</section>

<section class="card card--back" aria-label="Card back">
  <svg class="shape" width="540" height="309" viewBox="0 0 540 309" aria-hidden="true">
    <polygon points="250,309 300,232 540,196 540,309" fill="var(--green)"/>
  </svg>

  <div class="holder">
    <div class="holder-name">Martin Dellacroix</div>
    <div class="holder-title">Executive Vice President</div>
  </div>

  <div class="contact-band">
    <div class="contact-icons">
      <svg width="20" height="18" viewBox="0 0 20 18" aria-hidden="true">
        <rect width="20" height="18" rx="2" fill="var(--green)"/>
        <path d="M6 4 L8 4 L9 7 L7.6 8 C8.3 9.6 9.6 10.9 11.2 11.6 L12.2 10.2 L15 11.2 L15 13.2 C15 13.8 14.5 14.2 13.9 14.2 C9.2 13.8 5.4 10 5 5.3 C5 4.6 5.4 4 6 4 Z" fill="#fff"/>
      </svg>
      <svg width="20" height="18" viewBox="0 0 20 18" aria-hidden="true">
        <rect width="20" height="18" rx="2" fill="var(--green)"/>
        <rect x="4" y="5" width="12" height="8" fill="none" stroke="#fff" stroke-width="1.4"/>
        <path d="M4 5 L10 10 L16 5" fill="none" stroke="#fff" stroke-width="1.4"/>
      </svg>
    </div>
    <div class="contact-lines">
      <div>240-555-0187</div>
      <div>mdellacroix@brightvaleenergy.example</div>
    </div>
  </div>

  <div class="office">
    <div class="office-name">Brightvale Energy Company</div>
    <div>41 K ST NE Washington,</div>
    <div>DC 20017</div>
  </div>

  <div class="back-brand">
    <span class="brand-dot"></span>
    <div class="brand-text">
      <span class="brand-name">brightvale energy</span>
      <span class="brand-sub">Company</span>
    </div>
  </div>
</section>

</body>
</html>
```